Raising floral designer needs an artistic business card

I am an award winning floral designer wishing to transition from commercial wedding/event work to show designs as well as educating and consulting the art of flowers. My design style is the fusion of Ikebana and European floral art, so I wish my business card reflects it. I would like my card give people creative and energetic impression combined with the subtlety and gracefulness of the Eastern culture.
Target Market(s)
General public as well as related professionals
Industry/Entity Type
Floral
Contact Information for Business Card
Marla Dovien Holt NGPB, RTA.
Floral Artist and Consultant.
Phone: 417-296-7183.   email: marlapetals@kelvamail.com
Requirements
Must have
- color, floral/plant element, clean-looking
Nice to have
- a set with different color background/designs or shapes.
Should not have
- psychedelic colors and lines, illegible fonts.

```html
<!DOCTYPE html>
<html lang="en">
<head>
<meta charset="utf-8">
<title>Marla Dovien Holt — Business Card</title>
<link href="https://fonts.googleapis.com/css2?family=Marcellus&family=Questrial&display=swap" rel="stylesheet">
<style>
  :root {
    --page-bg: #f2f0ec;
    --card-cream: #f6e7cf;
    --card-cream-deep: #efdcbd;
    --gold: #b8862f;
    --gold-light: #e4c48a;
    --gold-dark: #8a6420;
    --ink: #2a2018;
    --photo-dark: #2f3a24;
    --photo-mid: #5b6b3c;
    --photo-warm: #9a5a2c;
  }
  * { margin: 0; padding: 0; box-sizing: border-box; }
  html, body {
    width: 1200px; height: 900px; overflow: hidden;
    background: var(--page-bg);
  }
  .canvas {
    position: relative; width: 1200px; height: 900px;
    display: flex; align-items: center; justify-content: center;
  }
  .card {
    position: relative; width: 980px; height: 560px;
    border-radius: 36px; overflow: hidden;
    background: linear-gradient(135deg, var(--card-cream) 0%, var(--card-cream-deep) 100%);
    box-shadow: 0 18px 40px rgba(0,0,0,0.18);
  }
  .card-art { position: absolute; inset: 0; }
  .identity {
    position: absolute; left: 40px; top: 40px; width: 560px;
    text-align: center;
  }
  .monogram {
    font-family: "Marcellus", serif;
    color: var(--gold);
    font-size: 96px; line-height: 1; letter-spacing: 4px;
  }
  .name {
    margin-top: 14px;
    font-family: "Marcellus", serif;
    color: var(--ink);
    font-size: 50px; line-height: 1;
  }
  .credentials {
    margin-top: 10px; padding-left: 120px;
    font-family: "Marcellus", serif;
    color: var(--ink);
    font-size: 18px; letter-spacing: 1px;
  }
  .tagline {
    position: absolute; left: 66px; top: 318px;
    font-family: "Questrial", sans-serif;
    color: var(--gold);
    font-size: 30px;
  }
  .contact {
    position: absolute; left: 62px; top: 440px;
    font-family: "Questrial", sans-serif;
    color: var(--ink);
    list-style: none;
  }
  .contact-item { display: flex; align-items: center; gap: 14px; }
  .contact-phone { font-size: 38px; }
  .contact-email { font-size: 31px; margin-top: 6px; }
  .contact-icon { width: 36px; height: 36px; flex: none; }
</style>
</head>
<body>
<main class="canvas">
  <article class="card">
    <svg class="card-art" viewBox="0 0 980 560" width="980" height="560">
      <defs>
        <linearGradient id="photo-tones" x1="0" y1="0" x2="0" y2="1">
          <stop offset="0" stop-color="#7d8a6a"/>
          <stop offset="0.3" stop-color="var(--photo-warm)"/>
          <stop offset="0.55" stop-color="var(--photo-mid)"/>
          <stop offset="1" stop-color="var(--photo-dark)"/>
        </linearGradient>
        <linearGradient id="gold-band" x1="0" y1="0" x2="1" y2="1">
          <stop offset="0" stop-color="var(--gold-dark)"/>
          <stop offset="0.5" stop-color="var(--gold-light)"/>
          <stop offset="1" stop-color="var(--gold)"/>
        </linearGradient>
      </defs>
      <path class="gold-band" d="M560 0 H640 C600 140 610 330 740 560 H700 C580 380 545 180 560 0 Z" fill="url(#gold-band)"/>
      <path class="photo-area" role="img" aria-label="Photo of a garden gazebo with a hanging floral installation of fruit and flowers above a dining table"
            d="M640 0 H980 V560 H740 C610 330 600 140 640 0 Z" fill="url(#photo-tones)"/>
    </svg>

    <header class="identity">
      <div class="monogram">MDH</div>
      <h1 class="name">Marla Dovien Holt</h1>
      <p class="credentials">NGPB, RTA.</p>
    </header>

    <p class="tagline">Floral Artist and Consultant.</p>

    <ul class="contact">
      <li class="contact-item contact-phone">
        <svg class="contact-icon" viewBox="0 0 24 24" aria-hidden="true">
          <path fill="var(--gold)" d="M6.6 2.5c.6-.4 1.4-.3 1.8.3l2 3c.4.6.3 1.3-.2 1.8l-1.4 1.2c.9 2 2.5 3.8 4.5 4.9l1.3-1.3c.5-.5 1.3-.6 1.8-.2l3 2c.6.4.8 1.2.4 1.8l-1.2 2c-.6 1-1.8 1.5-3 1.2C9.7 17.6 5.4 13.3 3.8 7.4c-.3-1.1.1-2.3 1-3z"/>
        </svg>
        <span>417-296-7183.</span>
      </li>
      <li class="contact-item contact-email">
        <svg class="contact-icon" viewBox="0 0 24 24" aria-hidden="true">
          <rect x="2" y="6" width="20" height="13" rx="1.5" fill="var(--gold)"/>
          <path d="M2.8 7 12 13.5 21.2 7" fill="none" stroke="var(--card-cream)" stroke-width="1.5"/>
        </svg>
        <span>marlapetals@kelvamail.com</span>
      </li>
    </ul>
  </article>
</main>
</body>
</html>
```